Vocational Mentor needs an impressive business card

1. I need a business card (or maybe three with identic look) to promote me and my three business titles/services:
- Vocational Mentor. I help people find their vocation and live happily from it. I use my 20 years of experience in business, management and psychology to help them identify the most efficient ways to make a living doing what they are passionate about.
- Business Angel. I help founders start a succesful business with minimum risks and costs. I use my 20 years of experience in sales, management and entrepreneurship to help them identify the most efficient ways, in terms of time and cost, to validate their business idea.
- Learning Designer. I design unique learning programs that produce long-term cognitive and behavioural changes to people and organisations. I use my 20 years of experience in learning, teaching and change management to create minimalist experiences and processes that allow them to change efficiently in their pursued direction.

2. I would like a two-sided business card, on the front with my name, contact details and titles, on the back the explanation of the services.
Updates

Hi all,

I updated my brief, included contacts info and give feedback on all designs I got. I am new on this platform so please tell me if you need anything else or if I don't use corectly the platform forms.

Kind regards,
Tudor

Hi all,

I shortened the services description by deleting the phrase "I call..."

Kind regards,
Tudor

Target Market(s)

Freelancers, startups, people and organization willing to invest in change through ultimate learning experiences

Industry/Entity Type

Business

Font styles to use
Serif

Requirements
Must have
• Front side: full name, titles, web site, email, phone like below:
Tudor Vasilache
Vocational Mentor, Business Angel, Learning Designer
info@tudorvasilache.example
www.tudorvasilache.example
+40-745-TUDORV
Nice to have
• Back side: the description of the services I provide as in the task description.
1/3: it would be nice if I can jam all three titles on the front side but then I need a solution to jam all three services on the back side.

```html
<!DOCTYPE html>
<html lang="en">
<head>
<meta charset="utf-8">
<title>Tudor Vasilache — Business Card</title>
<link href="https://fonts.googleapis.com/css2?family=Tinos:wght@400;700&family=Open+Sans:wght@400&display=swap" rel="stylesheet">
<style>
  :root {
    --backdrop: #e9e4de;
    --card-light: #ffffff;
    --card-light-shade: #ececec;
    --card-dark: #1f1e1f;
    --ink: #1c1c1c;
    --ink-soft: #3a3a3a;
    --rule: #555555;
    --silver-hi: #d9d9d9;
    --silver-lo: #6a6a6a;
  }
  html, body {
    margin: 0;
    padding: 0;
    width: 1200px;
    height: 565px;
    overflow: hidden;
    background: var(--backdrop);
  }
  .canvas {
    position: relative;
    width: 1200px;
    height: 565px;
  }
  .card {
    position: absolute;
    top: 140px;
    width: 500px;
    height: 286px;
    box-sizing: border-box;
    box-shadow: 0 6px 18px rgba(0,0,0,0.18);
  }
  /* Front side */
  .card--front {
    left: 70px;
    background: linear-gradient(160deg, var(--card-light-shade) 0%, var(--card-light) 45%);
  }
  .front__email {
    position: absolute;
    top: 78px;
    right: 26px;
    font: 9px "Open Sans", sans-serif;
    color: var(--ink-soft);
  }
  .front__name {
    position: absolute;
    left: 48px;
    top: 96px;
    margin: 0;
    font: 400 29px "Tinos", serif;
    letter-spacing: 0.5px;
    color: var(--ink);
  }
  .front__titles {
    position: absolute;
    left: 48px;
    top: 164px;
    width: 230px;
    margin: 0;
    font: 10.5px/1.3 "Open Sans", sans-serif;
    color: var(--ink);
  }
  .front__phone {
    position: absolute;
    left: 48px;
    top: 202px;
    display: flex;
    align-items: center;
    gap: 8px;
    font: 12px "Open Sans", sans-serif;
    color: var(--ink);
  }
  .front__phone svg { width: 9px; height: 11px; }
  .front__rule {
    position: absolute;
    left: 0;
    right: 0;
    top: 226px;
    height: 2px;
    background: var(--rule);
  }
  /* Back side */
  .card--back {
    left: 630px;
    background: var(--card-dark);
    display: flex;
    align-items: center;
    justify-content: center;
  }
  .back__name {
    margin: 0;
    font: 700 36px "Tinos", serif;
    letter-spacing: 0.5px;
    background: linear-gradient(90deg, var(--silver-hi) 0%, var(--silver-hi) 35%, var(--silver-lo) 100%);
    -webkit-background-clip: text;
    background-clip: text;
    color: transparent;
  }
</style>
</head>
<body>
<main class="canvas">
  <section class="card card--front" aria-label="Front side">
    <span class="front__email">info@tudorvasilache.example</span>
    <h1 class="front__name">Tudor Vasilache</h1>
    <p class="front__titles">Vocational Mentor, Business Angel, Learning Designer</p>
    <div class="front__phone">
      <svg viewBox="0 0 9 11" aria-hidden="true">
        <rect x="0.5" y="0.5" width="8" height="10" rx="1" fill="none" stroke="#555" stroke-width="1"/>
        <rect x="2" y="2" width="5" height="4" fill="#888"/>
        <circle cx="4.5" cy="8.3" r="0.9" fill="#555"/>
      </svg>
      <span>+40-745-TUDORV</span>
    </div>
    <div class="front__rule"></div>
  </section>
  <section class="card card--back" aria-label="Back side">
    <h2 class="back__name">Tudor Vasilache</h2>
  </section>
</main>
</body>
</html>
```